Hotel Business Card Project

Amber Crest Hotel will be a premium boutique hotel in Dhaka, Bangladesh. The hotel will offer the finest amenities and facilities available on the market, and the cost per room investment will far exceed other 5-star hotels currently in the market.

As a result, we wanted the business card to reflect that premium/luxurious/upscale feel, and also be elegant and hospitable at the same time.

The name 'Amber Crest' is derived from the fact that Bangladesh has 6 distinct seasons (you can get more information online if required, or contact me about it). The leaves in the logo has the tree because trees give people shade, protection and safety (just like our hotel would try to give).

Target Market(s)

Business professionals, guests

Industry/Entity Type

Investment

Requirements
Must have
• Elegant, Classy and very attractive business card.

Must be editable to enter specific Names, Positions, Phone numbers and email later on.
Nice to have
• The address would be: House 47, Road 23, Lakeview 5, Dhaka 1208, Bangladesh

Slogan- Luxury Redefined

```html
<!DOCTYPE html>
<html lang="en">
<head>
<meta charset="UTF-8">
<title>Amber Crest Hotel – Business Card</title>
<link rel="stylesheet" href="https://fonts.googleapis.com/css2?family=Crimson+Text:wght@400;600&display=swap">
<style>
  :root {
    --backdrop: #7a4e2d;
    --maroon: #560a0c;
    --paper: #ffffff;
    --brand-grey: #6e6a6c;
    --brand-grey-light: #8f8688;
    --rule: #8a6a6a;
    --address: #b99c9c;
    --lime: #cfd22a;
    --muted-text: #c4aaaa;
    --mark: #c98a3c;
  }
  * { margin: 0; padding: 0; box-sizing: border-box; }
  html, body { width: 1200px; height: 446px; overflow: hidden; }
  body {
    background: var(--backdrop);
    font-family: "Crimson Text", Georgia, serif;
    position: relative;
  }
  .card {
    position: absolute;
    top: 53px;
    width: 536px;
    height: 331px;
    border-radius: 16px;
    overflow: hidden;
  }
  .card--back { left: 57px; background: var(--maroon); }
  .card--front { left: 634px; background: var(--maroon); }

  .brand {
    position: absolute;
    left: 0; right: 0;
    top: 20px;
    text-align: center;
  }
  .brand__mark {
    display: block;
    width: 120px; height: 120px;
    margin: 0 auto 14px;
    border-radius: 50%;
    background: var(--mark);
  }
  .brand__name {
    font-size: 31px;
    letter-spacing: 1px;
    color: var(--brand-grey-light);
    line-height: 1;
  }
  .card--front .brand__name { color: var(--brand-grey); }

  .back__rule {
    position: absolute;
    left: 51px; right: 51px;
    top: 220px;
    height: 2px;
    background: var(--rule);
  }
  .back__address {
    position: absolute;
    left: 40px; right: 40px;
    top: 244px;
    text-align: center;
    font-size: 20px;
    line-height: 27px;
    color: var(--address);
  }

  .front__top {
    position: absolute;
    left: 0; right: 0; top: 0;
    height: 202px;
    background: var(--paper);
  }
  .person {
    position: absolute;
    left: 0; width: 256px;
    top: 236px;
    text-align: center;
  }
  .person__name {
    font-size: 27px;
    color: var(--lime);
    line-height: 1;
  }
  .person__role {
    font-size: 17px;
    color: var(--muted-text);
    margin-top: 8px;
  }
  .front__divider {
    position: absolute;
    left: 256px;
    top: 221px;
    width: 2px; height: 99px;
    background: var(--rule);
  }
  .contact {
    position: absolute;
    left: 290px;
    display: flex;
    align-items: center;
    color: var(--muted-text);
  }
  .contact--phone { top: 224px; }
  .contact--email { top: 269px; }
  .contact__icon {
    width: 32px; height: 32px;
    border-radius: 50%;
    background: var(--lime);
    display: flex; align-items: center; justify-content: center;
    flex: none;
    color: #6b6b20;
    font-size: 22px;
    line-height: 1;
  }
  .contact__text { margin-left: 0; text-align: center; }
  .contact--phone .contact__text { width: 210px; font-size: 21px; }
  .contact--email .contact__text { width: 210px; font-size: 15px; }
</style>
</head>
<body>
  <section class="card card--back" aria-label="Card back">
    <div class="brand">
      <span class="brand__mark" aria-hidden="true"></span>
      <div class="brand__name">Amber Crest Hotel</div>
    </div>
    <div class="back__rule"></div>
    <p class="back__address">House 47, Road 23, Lakeview 5, Dhaka 1208,<br>Bangladesh</p>
  </section>

  <section class="card card--front" aria-label="Card front">
    <div class="front__top"></div>
    <div class="brand">
      <span class="brand__mark" aria-hidden="true"></span>
      <div class="brand__name">Amber Crest Hotel</div>
    </div>
    <div class="person">
      <div class="person__name">Daniel Hart</div>
      <div class="person__role">executive manager</div>
    </div>
    <div class="front__divider"></div>
    <div class="contact contact--phone">
      <span class="contact__icon">
        <svg width="18" height="18" viewBox="0 0 24 24" aria-hidden="true">
          <path fill="#6b6b20" d="M6.6 10.8a15.1 15.1 0 0 0 6.6 6.6l2.2-2.2a1 1 0 0 1 1-.25 11.4 11.4 0 0 0 3.6.57 1 1 0 0 1 1 1V20a1 1 0 0 1-1 1A17 17 0 0 1 3 4a1 1 0 0 1 1-1h3.5a1 1 0 0 1 1 1c0 1.25.2 2.45.57 3.57a1 1 0 0 1-.25 1z"/>
        </svg>
      </span>
      <span class="contact__text">+000 000 000</span>
    </div>
    <div class="contact contact--email">
      <span class="contact__icon">@</span>
      <span class="contact__text">d.hart@ambercrest.com</span>
    </div>
  </section>
</body>
</html>
```